Namecard Designs+Logo for a High End Automobile Company

We need a new business card for our company called Velta Motorhof.

www.veltamotorhof.example.sg
Our new website will be up in 2.5 months time.

We sell used and brand new continental cars like Korvane, QTL, Dravell, Solbrini and etc. Currently we are operating from 2 offices in Singapore and United Kingdom.

We want a design which is serious. We are open to colours but try to keep it at a maximum of 3 colours.

We prefer something simple and minimal. We are open to 2 sides printing or even 2 sided namecards. Both UK and Singapore company offices address must be in; either side by side, front and back, or even 2 sided cards.

The logo can be a text logo, emblem, abstract, pictorial or combination.

We are printing with Pribo.com so please kindly follow the printing guideline.

http://uk.pribo.example/help/faq/templates-and-guidelines.html

Rich and Car Enthusiasts

Printing

Must have
• Our 2 offices; UK and Singapore.

Our slogan which is " The Automobile Specialist"
Should not have
• Not more than 3 colours

```html
<!DOCTYPE html>
<html lang="en">
<head>
<meta charset="utf-8">
<title>Velta Motorhof – Business Card</title>
<link rel="stylesheet" href="https://fonts.googleapis.com/css2?family=Poiret+One&display=swap">
<style>
  :root {
    --bg-light: #5c5c5c;
    --bg-mid: #3a3a3a;
    --bg-dark: #262626;
    --ring: #2b2b2b;
    --text: #ffffff;
    --brand: #e4e4e4;
    --muted: #bdbdbd;
  }
  * { margin: 0; padding: 0; box-sizing: border-box; }
  html, body {
    width: 800px;
    height: 1200px;
    overflow: hidden;
    background: var(--bg-dark);
  }
  .card {
    position: relative;
    width: 800px;
    height: 1200px;
    overflow: hidden;
    background: radial-gradient(circle at 163px 290px, var(--bg-light) 0%, var(--bg-mid) 40%, var(--bg-dark) 100%);
    font-family: "Poiret One", "Century Gothic", sans-serif;
    color: var(--text);
    -webkit-text-stroke: 0.6px currentColor;
  }
  .rings {
    position: absolute;
    left: 0;
    top: 0;
  }
  .brand {
    position: absolute;
    left: 80px;
    top: 135px;
    font-size: 52px;
    color: var(--brand);
    white-space: nowrap;
    letter-spacing: 1px;
  }
  .slogan {
    position: absolute;
    left: 84px;
    top: 210px;
    font-size: 24px;
    color: var(--muted);
    -webkit-text-stroke: 0.3px currentColor;
    letter-spacing: 2px;
    white-space: nowrap;
  }
  .holder {
    position: absolute;
    left: 0;
    width: 800px;
    text-align: center;
    white-space: nowrap;
  }
  .holder-name {
    top: 336px;
    font-size: 56px;
    letter-spacing: 5px;
  }
  .holder-position {
    top: 420px;
    padding-left: 28px;
    font-size: 36px;
  }
  .contact {
    position: absolute;
    left: 0;
    top: 862px;
    width: 800px;
    list-style: none;
    font-size: 36px;
    line-height: 50px;
    letter-spacing: 0.5px;
    text-align: center;
    padding-left: 62px;
    white-space: nowrap;
  }
</style>
</head>
<body>
<div class="card">
  <svg class="rings" width="800" height="1200" viewBox="0 0 800 1200" aria-hidden="true">
    <g fill="none" stroke="var(--ring)" stroke-width="26">
      <circle cx="655" cy="685" r="370"/>
      <circle cx="655" cy="685" r="285"/>
      <circle cx="655" cy="685" r="232"/>
    </g>
  </svg>

  <div class="brand">Velta Motorhof</div>
  <div class="slogan">The Automobile Specialist</div>

  <div class="holder holder-name">your name here</div>
  <div class="holder holder-position">Position</div>

  <ul class="contact">
    <li class="contact-address-sg">address SG:xxxxxxxxxxxxxxxx</li>
    <li class="contact-address-uk">address UK:xxxxxxxxxxxxxxxx</li>
    <li class="contact-website">website:xxxxxxxxxxxxxxxxxx</li>
    <li class="contact-email">email:xxxxxxxxxxxxxxxxxxxx</li>
    <li class="contact-phone">phone:xxxxxxxxxxxxxxxxxx</li>
  </ul>
</div>
</body>
</html>
```